Sex Trafficked women Empowered Business Card Design Project

I would like a two-sided business card. On the front, please include: Marta Oberlin, Executive Director 555-284-7316, www.tallowcrest.org, marta@tallowcrest.org and logo.

On the back:
Vision
Survivors of sexual exploitation live free, fulfilling their God-given purpose.

Perhaps a QR code to direct them to the website: www.tallowcrest.org

I want to try a deeper color for the logo. i have added these files.

My desire is to communicate hope, freedom and new life.
Updates

i decided to ask for business card designs with a deeper toned logo. see new files attached

i have placed the vertical logo as an option, but i would still want the logo with tagline used.

Target Market(s)

I want a professional look to appeal to donors who have a heart to help sexually exploited women. I chose a logo that was light enough to look good on a variety of backgrounds. I do want the logo to catch attention.

Industry/Entity Type

Business

Font styles to use
Serif

Requirements
Must have
• i want to be able to read the tagline. Also, the design should match the look and feel of the logo.

Nice to have
• Since there isn't much text on the back, feel free to be a bit more creative. I still want a professional look.

```html
<!DOCTYPE html>
<html lang="en">
<head>
<meta charset="utf-8">
<title>Tallowcrest – Business Card</title>
<link rel="stylesheet" href="https://fonts.googleapis.com/css2?family=Tinos:ital,wght@0,400;0,700;1,400&display=swap">
<style>
  :root {
    --page: #ffffff;
    --card-navy: #001a6b;
    --ink-white: #ffffff;
    --mark-blue: #1f6fff;
    --accent-gold: #ffd400;
  }
  * { box-sizing: border-box; margin: 0; padding: 0; }
  html, body {
    width: 1200px; height: 1000px; overflow: hidden;
    background: var(--page);
    font-family: "Tinos", "Times New Roman", serif;
  }
  .canvas { position: relative; width: 1200px; height: 1000px; }
  .card {
    position: absolute; left: 58px; top: 205px;
    width: 1086px; height: 590px;
    background: var(--card-navy);
    border-radius: 52px;
    color: var(--ink-white);
  }
  .card__divider {
    position: absolute; left: 801px; top: 0;
    width: 2px; height: 100px; background: var(--ink-white);
  }
  .card__person { position: absolute; left: 826px; top: 42px; }
  .person__name { font-weight: 700; font-size: 27px; line-height: 1.2; letter-spacing: 0.5px; }
  .person__title { font-size: 22px; line-height: 1.45; }
  .brand {
    position: absolute; left: 164px; top: 215px;
    display: flex; align-items: center;
  }
  .brand__dot {
    width: 182px; height: 182px; border-radius: 50%;
    background: var(--mark-blue);
    box-shadow: inset 0 0 0 6px var(--accent-gold);
    flex: none;
  }
  .brand__text { margin-left: 24px; padding-top: 14px; }
  .brand__name {
    font-size: 64px; font-weight: 400; line-height: 1;
    letter-spacing: 4px; text-transform: uppercase;
    color: var(--ink-white); white-space: nowrap;
  }
  .brand__tagline {
    margin-top: 8px; text-align: right; padding-right: 14px;
    font-style: italic; font-size: 27px; color: var(--ink-white);
    white-space: nowrap;
  }
  .contact {
    position: absolute; left: 85px; top: 510px;
    display: flex; align-items: center; gap: 14px;
    font-size: 28px; white-space: nowrap;
  }
  .contact__item { display: flex; align-items: center; gap: 9px; }
  .contact__sep { margin: 0 6px; }
  .contact__icon { width: 27px; height: 27px; fill: none; stroke: var(--ink-white); }
</style>
</head>
<body>
<div class="canvas">
  <section class="card">
    <div class="card__divider"></div>
    <div class="card__person">
      <p class="person__name">Marta Oberlin</p>
      <p class="person__title">Executive Director</p>
    </div>

    <div class="brand">
      <div class="brand__dot"></div>
      <div class="brand__text">
        <p class="brand__name">Tallowcrest</p>
        <p class="brand__tagline">Where new life takes wing</p>
      </div>
    </div>

    <div class="contact">
      <span class="contact__item">
        <svg class="contact__icon" viewBox="0 0 24 24" aria-hidden="true"><path d="M5 2h4l2 5-3 2c1 3 3 5 6 6l2-3 5 2v4c0 2-1 3-3 3C10 21 3 14 3 5c0-2 1-3 2-3z" fill="#fff" stroke="none"/></svg>
        555-284-7316
      </span>
      <span class="contact__sep">|</span>
      <span class="contact__item">
        <svg class="contact__icon" viewBox="0 0 24 24" aria-hidden="true" stroke-width="1.6"><circle cx="12" cy="12" r="10"/><ellipse cx="12" cy="12" rx="4.5" ry="10"/><path d="M2 12h20M4 7h16M4 17h16"/></svg>
        www.tallowcrest.org
      </span>
      <span class="contact__sep">|</span>
      <span class="contact__item">
        <svg class="contact__icon" viewBox="0 0 26 20" aria-hidden="true"><rect x="1" y="3" width="24" height="15" fill="#fff" stroke="none"/><path d="M1 3l12 9 12-9M1 18l9-7M25 18l-9-7" stroke="#001a6b" stroke-width="1.6"/></svg>
        marta@tallowcrest.org
      </span>
    </div>
  </section>
</div>
</body>
</html>
```